Media and Film Company Needs a New Website

We produce highly stylized commercials and film pieces for our clients. We also produce live events, both corporate and theatrical. Looking for a site that can show off our client videos - have a polished way to show off our team, and be able to create pages to highlight our clients and give a full overview of our project/process with them. We design simple website for some of our clients - so we are very wordpress familiar, and would like something that doesn't feel like a template.

Target Market(s)

content creators, creative directors, production teams, marketing agencies

Industry/Entity Type

Film Production

Number of Pages Required

4 page

Font styles to use
Sans Serif

Requirements
Must have
• slick looking video embed (from YT or Vimeo)
• project pages - client snapshot (what we did for them, how we did it)
• nice landing page, have our company video reel on the page
• testimonials
• contact page
• ability to have photos as a background if we want
Nice to have
• polished clean look - look to our logo colors and linear elements
• we produce very stylized videos for our clients and our website should reflect that
Should not have
• template look or feel to it- please bring your flare to the project!
• take a look at our current site - brelvostudio.com we need a better way to highlight our work and our clients

```html
<!DOCTYPE html>
<html lang="en">
<head>
<meta charset="utf-8">
<title>Brelvo Studio &amp; Entertainment</title>
<link href="https://fonts.googleapis.com/css2?family=Hind:wght@300;400;500;600;700&display=swap" rel="stylesheet">
<style>
:root{
  --cyan:#2b93d1;
  --yellow:#f3c01c;
  --magenta:#d8197f;
  --charcoal:#404040;
  --ink:#2d2d2d;
  --text:#6b6b6b;
  --soft:#f3f3f3;
  --line:#e2e2e2;
  --footer:#333333;
  --footer-base:#232323;
  --white:#ffffff;
}
*{box-sizing:border-box;margin:0;padding:0}
html,body{width:1200px;height:3719px;overflow:hidden}
body{font-family:"Hind",Arial,sans-serif;color:var(--text);background:var(--white);position:relative}
.section-title{font-size:32px;font-weight:400;color:var(--ink);text-align:center;letter-spacing:.5px}
.outline-btn{display:block;width:298px;height:58px;line-height:60px;border:2px solid var(--magenta);text-align:center;color:var(--ink);font-size:17px;font-weight:500;letter-spacing:.5px;text-transform:uppercase;margin:0 auto}

/* hero */
.hero{position:relative;height:664px;overflow:hidden}
.hero-photo{position:absolute;inset:0;background:linear-gradient(180deg,#8fa08a 0%,#6e8a5c 35%,#4a4d4a 70%,#3a3b3c 100%)}
.hero-shade{position:absolute;inset:0;background:rgba(20,20,20,.25)}
.brand{position:absolute;left:74px;top:36px;display:flex;align-items:center;gap:10px;color:var(--white);font-size:26px;font-weight:700;letter-spacing:1px}
.brand-mark{width:14px;height:14px;background:var(--magenta)}
.main-nav{position:absolute;right:75px;top:38px;display:flex;gap:36px}
.main-nav a{color:var(--white);font-size:13px;font-weight:700;text-transform:uppercase;letter-spacing:.5px;text-decoration:none;line-height:22px;white-space:nowrap}
.main-nav a.active{color:var(--yellow);border-left:3px solid var(--yellow);padding-left:12px}
.hero-title{position:absolute;top:268px;left:0;right:0;text-align:center;color:var(--white);font-size:49px;font-weight:700;line-height:52px;letter-spacing:1px}
.hero-btn{position:absolute;left:497px;top:410px;width:206px;height:56px;line-height:58px;background:var(--magenta);color:var(--white);text-align:center;font-size:16px;font-weight:700;letter-spacing:.5px}
.hero-dots{position:absolute;left:565px;top:615px;display:flex;gap:8px}
.hero-dots span{width:10px;height:10px;border-radius:50%;background:var(--white)}
.hero-dots span.on{background:var(--yellow)}

/* about */
.about{position:relative;height:456px}
.about-copy{position:absolute;left:74px;top:42px;width:530px}
.about-copy h2{font-size:32px;font-weight:500;color:var(--ink);line-height:36px}
.about-brand{display:flex;align-items:center;gap:8px;margin:14px 0 28px;font-size:24px;font-weight:700;color:var(--ink);letter-spacing:1px}
.about-brand i{width:12px;height:12px;background:var(--magenta)}
.about-copy p{font-size:15px;line-height:24px;margin-bottom:6px}
.reel{position:absolute;left:615px;top:55px;width:510px;height:330px;background:#161616}
.reel-name{position:absolute;left:0;right:0;top:86px;text-align:center;color:var(--white);font-size:24px;font-weight:700;letter-spacing:1px;white-space:nowrap}
.reel-name i{display:inline-block;width:13px;height:13px;background:var(--magenta);margin-right:12px;vertical-align:2px}
.reel-title{position:absolute;left:0;right:0;top:170px;text-align:center;color:#e6e6e6;font-size:50px;font-weight:300;line-height:56px}
.reel-bar{position:absolute;left:10px;right:10px;bottom:10px;height:24px;display:flex;align-items:center;gap:10px}
.reel-bar .track{flex:1;height:4px;background:#555}
.reel-bar .time{width:26px;height:12px;background:#888;border-radius:2px}

/* services */
.services{position:relative;height:591px;background:var(--soft)}
.services .section-title{position:absolute;top:52px;left:0;right:0}
.tile-grid{position:absolute;left:342px;top:122px;width:516px;display:grid;grid-template-columns:258px 258px;grid-template-rows:202px 202px}
.tile{color:var(--white);text-align:center;font-weight:700;font-size:22px;line-height:25px;text-transform:uppercase;padding-top:30px}
.tile svg{display:block;margin:0 auto 18px}
.tile-film{background:var(--cyan)}
.tile-live{background:var(--yellow)}
.tile-pr{background:var(--magenta)}
.tile-events{background:var(--charcoal)}
.skill-list{position:absolute;list-style:none}
.skill-list li{font-size:15px;line-height:22px;color:#555;margin-bottom:15px;padding-left:28px;position:relative;white-space:nowrap}
.skill-list li::before{content:"";position:absolute;left:0;top:3px;width:13px;height:13px;border:2px solid var(--cyan);border-radius:50%}
.skill-list li::after{content:"";position:absolute;left:4px;top:8px;width:5px;height:5px;border-top:2px solid var(--cyan);border-right:2px solid var(--cyan);transform:rotate(45deg);margin-left:-1px}
.list-a{left:74px;top:158px}
.list-b{left:74px;top:357px}
.list-c{left:888px;top:137px}
.list-d{left:888px;top:357px}

/* videos */
.videos{position:relative;height:713px}
.videos .section-title{position:absolute;top:68px;left:0;right:0}
.thumb{position:absolute}
.thumb-main{left:74px;top:131px;width:514px;height:412px;background:linear-gradient(120deg,#2d4fa8,#1c2f6e 55%,#4a4f5e)}
.thumb-a{left:600px;top:131px;width:255px;height:203px;background:linear-gradient(180deg,#3c4a6a,#1e2433)}
.thumb-b{left:868px;top:131px;width:257px;height:203px;background:linear-gradient(180deg,#9aa3a0,#6f7f62)}
.thumb-c{left:600px;top:342px;width:255px;height:201px;background:linear-gradient(180deg,#efeeea,#d9d7d0)}
.thumb-d{left:868px;top:342px;width:257px;height:201px;background:linear-gradient(180deg,#6a5d4e,#3b342c)}
.play{position:absolute;left:50%;top:50%;transform:translate(-50%,-50%);background:rgba(255,255,255,.85);border-radius:8px}
.play::after{content:"";position:absolute;left:50%;top:50%;transform:translate(-35%,-50%);border-style:solid;border-color:transparent transparent transparent #3a63b8}
.play-lg{width:92px;height:62px}
.play-lg::after{border-width:15px 0 15px 24px}
.play-sm{width:58px;height:40px}
.play-sm::after{border-width:10px 0 10px 16px}
.videos .outline-btn{position:absolute;left:451px;top:587px}

/* testimonials */
.testimonials{position:relative;height:452px;background:var(--soft)}
.testimonials .section-title{position:absolute;top:50px;left:0;right:0}
.quote{position:absolute;top:114px;width:330px}
.quote p{font-size:16px;line-height:27px;font-style:italic;color:#666}
.quote-author{display:flex;gap:14px;margin-top:18px;align-items:flex-start}
.quote-icon{display:flex;width:44px;min-width:44px;height:44px;border-radius:50%;background:var(--cyan);align-items:center;justify-content:center}
.quote-author b{display:block;color:var(--cyan);font-size:14px;font-weight:600;line-height:20px}
.quote-author .role{display:block;font-size:13px;line-height:18px;color:#666}
.q1{left:74px}.q2{left:446px}.q3{left:800px}
.t-dots{position:absolute;left:567px;top:395px;display:flex;gap:7px}
.t-dots span{width:10px;height:10px;border-radius:50%;background:#777}
.t-dots span.on{background:var(--magenta)}

/* clients */
.clients{position:relative;height:478px}
.clients .section-title{position:absolute;top:66px;left:0;right:0}
.client-grid{position:absolute;left:74px;top:124px;width:1051px;display:grid;grid-template-columns:repeat(4,253px);grid-template-rows:79px 79px;column-gap:13px;row-gap:12px}
.client{border:1px solid var(--line);display:flex;align-items:center;justify-content:center;font-size:22px;font-weight:700;text-transform:uppercase;letter-spacing:.5px;white-space:nowrap}
.c-red{color:#b8322d}.c-dark{color:#1e2a3a}.c-teal{color:#2b9d8f}.c-wine{color:#8d1f2b}.c-orange{color:#e0602a}
.slider-arrow{position:absolute;top:190px;width:14px;height:14px;border-left:3px solid #aaa;border-bottom:3px solid #aaa}
.arrow-left{left:52px;transform:rotate(45deg)}
.arrow-right{right:52px;transform:rotate(-135deg)}
.clients .outline-btn{position:absolute;left:451px;top:342px}

/* footer */
.site-footer{position:relative;height:295px;background:var(--footer);color:#d0d0d0}
.footer-col{position:absolute;top:50px}
.footer-col h4{color:var(--white);font-size:15px;font-weight:600;text-transform:uppercase;letter-spacing:.5px;margin-bottom:14px}
.site-map{left:74px}
.site-map a{display:block;color:#cfcfcf;font-size:13px;line-height:29px;text-decoration:none}
.contact{left:300px}
.contact .co{color:var(--yellow);font-size:14px;font-weight:600;line-height:20px}
.contact p{font-size:13px;line-height:20px}
.contact .row{display:flex;align-items:center;gap:12px;font-size:13px;margin-top:10px}
.map{position:absolute;left:543px;top:50px;width:280px;height:173px;background:linear-gradient(135deg,#eef0ea,#dfe3d8)}
.newsletter{left:885px;width:240px}
.newsletter .field{width:240px;height:44px;background:var(--white);font-size:12px;color:#888;padding:15px 14px;text-transform:uppercase}
.newsletter .send{margin:14px 0 0 auto;width:88px;height:40px;line-height:42px;background:var(--magenta);color:var(--white);font-size:13px;font-weight:600;text-align:center;text-transform:uppercase}
.footer-base{position:relative;height:70px;background:var(--footer-base);color:#8a8a8a;font-size:12px}
.footer-base .copy{position:absolute;left:74px;top:28px}
.social{position:absolute;right:75px;top:27px;display:flex;gap:14px}
.social span{width:16px;height:16px;border-radius:50%;background:#9a9a9a}
</style>
</head>
<body>

<header class="hero">
  <div class="hero-photo" role="img" aria-label="Film crew with boom microphone and reflector shooting outdoors on a parking lot"></div>
  <div class="hero-shade"></div>
  <div class="brand"><span class="brand-mark"></span>BRELVO STUDIO</div>
  <nav class="main-nav">
    <a class="active" href="#">Home</a>
    <a href="#">Portfolio</a>
    <a href="#">About Brelvo</a>
    <a href="#">Testimonials</a>
    <a href="#">Press</a>
    <a href="#">Contact Us</a>
  </nav>
  <h1 class="hero-title">WELCOME TO<br>BRELVO STUDIO &amp; ENTERTAINMENT</h1>
  <a class="hero-btn">VIEW PORTFOLIO</a>
  <div class="hero-dots"><span class="on"></span><span class="on"></span><span></span><span></span></div>
</header>

<section class="about">
  <div class="about-copy">
    <h2>ABOUT</h2>
    <div class="about-brand"><i></i>BRELVO STUDIO</div>
    <p>Brelvo Studio &amp; Entertainment provides full-service campaigns in film and media production, live entertainment &amp; theatrical production, marketing &amp; advertising, and event management in the DC metro area.</p>
    <p>Founded in 2009, Brelvo Studio &amp; Entertainment has built a reputation working for clients including the National Screen Academy, Summit Forum, Harlow Music, Riverbend Community Resources, and Clearview Events.</p>
  </div>
  <div class="reel">
    <div class="reel-name"><i></i>BRELVO STUDIO &amp; ENTERTAINMENT</div>
    <div class="reel-title">2015 Demo Reel</div>
    <div class="reel-bar">
      <svg width="12" height="14" viewBox="0 0 12 14"><path d="M0 0L12 7L0 14Z" fill="#ddd"/></svg>
      <span class="time"></span><span class="track"></span><span class="time"></span>
    </div>
  </div>
</section>

<section class="services">
  <h2 class="section-title">WHAT WE DO</h2>
  <ul class="skill-list list-a"><li>Pro Design Software</li><li>Motion Graphics</li><li>4k Workflow</li><li>Direct To Web/Video Channels</li></ul>
  <ul class="skill-list list-b"><li>Theatrical Producing</li><li>Production Management</li><li>Lighting &amp; Video Design</li><li>Audio System Design</li></ul>
  <ul class="skill-list list-c"><li>Branding</li><li>Social Media</li><li>Media Relations &amp; Outreach</li><li>Street Teams</li></ul>
  <ul class="skill-list list-d"><li>Event production</li><li>Staffing &amp; hiring</li><li>Manage rfps</li><li>Sponsor relations</li></ul>
  <div class="tile-grid">
    <div class="tile tile-film">
      <svg width="70" height="66" viewBox="0 0 70 66" fill="#fff"><circle cx="18" cy="14" r="12"/><circle cx="44" cy="14" r="12"/><rect x="4" y="30" width="44" height="28" rx="3"/><path d="M50 38L66 30V58L50 50Z"/></svg>
      Film &amp;<br>Media Production
    </div>
    <div class="tile tile-live">
      <svg width="62" height="66" viewBox="0 0 62 66" fill="none" stroke="#fff" stroke-width="5"><path d="M20 4L31 16L42 4"/><rect x="4" y="18" width="54" height="40" rx="4"/><rect x="13" y="27" width="36" height="22" rx="2"/></svg>
      Live<br>Production
    </div>
    <div class="tile tile-pr">
      <svg width="72" height="66" viewBox="0 0 72 66" fill="#fff"><circle cx="22" cy="12" r="9"/><path d="M12 24H32L50 16V44L32 36H28V62H18V36H12Z"/><path d="M56 22L66 18M56 30H68M56 38L66 42" stroke="#fff" stroke-width="3"/></svg>
      PR, Marketing &amp;<br>Advertising
    </div>
    <div class="tile tile-events">
      <svg width="60" height="66" viewBox="0 0 60 66" fill="none" stroke="#fff" stroke-width="4"><rect x="4" y="10" width="52" height="50" rx="3"/><path d="M16 4V16M44 4V16M4 24H56M4 36H56M4 48H56M17 24V60M30 24V60M43 24V60"/></svg>
      Events<br>Production
    </div>
  </div>
</section>

<section class="videos">
  <h2 class="section-title">CLIENT VIDEOS</h2>
  <div class="thumb thumb-main" role="img" aria-label="Interview video still of two men in a studio"><span class="play play-lg"></span></div>
  <div class="thumb thumb-a" role="img" aria-label="Video still of a theater audience facing a stage"><span class="play play-sm"></span></div>
  <div class="thumb thumb-b" role="img" aria-label="Video still of an athlete on a sports field"><span class="play play-sm"></span></div>
  <div class="thumb thumb-c" role="img" aria-label="Video still of a community organization sign"><span class="play play-sm"></span></div>
  <div class="thumb thumb-d" role="img" aria-label="Interview video still of a restaurant executive"><span class="play play-sm"></span></div>
  <a class="outline-btn">View All Videos</a>
</section>

<section class="testimonials">
  <h2 class="section-title">TESTIMONIALS</h2>
  <div class="quote q1">
    <p>“ Thank you very much for all the hard work and creativity that you devoted to the RCR video, which was moving and uplifting and captured the essence of what we try to do so very well...”</p>
    <div class="quote-author"><span class="quote-icon"><svg width="20" height="16" viewBox="0 0 20 16" fill="#fff"><path d="M0 8Q0 1 7 0V3Q4 4 4 7H8V16H0ZM12 8Q12 1 19 0V3Q16 4 16 7H20V16H12Z"/></svg></span><div><b>Daniel Moore</b><span class="role">Executive Director, Riverbend Community Resources</span></div></div>
  </div>
  <div class="quote q2">
    <p>“ Thank you very much for all the hard work and creativity that you devoted to the RCR video, which was moving and uplifting and captured the essence of what we try to do so very well...”</p>
    <div class="quote-author"><span class="quote-icon"><svg width="20" height="16" viewBox="0 0 20 16" fill="#fff"><path d="M0 8Q0 1 7 0V3Q4 4 4 7H8V16H0ZM12 8Q12 1 19 0V3Q16 4 16 7H20V16H12Z"/></svg></span><div><b>Daniel Moore</b><span class="role">Executive Director, Riverbend Community Resources</span></div></div>
  </div>
  <div class="quote q3">
    <p>“ Thank you very much for all the hard work and creativity that you devoted to the RCR video, which was moving and uplifting and captured the essence of what we try to do so very well...”</p>
    <div class="quote-author"><span class="quote-icon"><svg width="20" height="16" viewBox="0 0 20 16" fill="#fff"><path d="M0 8Q0 1 7 0V3Q4 4 4 7H8V16H0ZM12 8Q12 1 19 0V3Q16 4 16 7H20V16H12Z"/></svg></span><div><b>Daniel Moore</b><span class="role">Executive Director, Riverbend Community Resources</span></div></div>
  </div>
  <div class="t-dots"><span class="on"></span><span></span><span></span><span></span></div>
</section>

<section class="clients">
  <h2 class="section-title">OUR CLIENTS</h2>
  <span class="slider-arrow arrow-left"></span>
  <span class="slider-arrow arrow-right"></span>
  <div class="client-grid">
    <div class="client c-red">NSA Docs</div>
    <div class="client c-dark">Tall Oak Films</div>
    <div class="client c-wine">Harlow Music</div>
    <div class="client c-dark">Summit Forum</div>
    <div class="client c-teal">Bright Paths</div>
    <div class="client c-red">Clearview</div>
    <div class="client c-wine">Ashford School</div>
    <div class="client c-orange">Norvec</div>
  </div>
  <a class="outline-btn">View All Clients</a>
</section>

<footer>
  <div class="site-footer">
    <div class="footer-col site-map">
      <h4>Site Map</h4>
      <a>Home</a><a>Portfolio</a><a>About Brelvo</a><a>Testimonials</a><a>Press</a><a>Contact Us</a>
    </div>
    <div class="footer-col contact">
      <h4>Contact Us</h4>
      <div class="co">Brelvo Studio &amp; Entertainment</div>
      <p>4410 Elm Street<br>#210 Fairview, MD 20900</p>
      <div class="row"><svg width="12" height="12" viewBox="0 0 12 12" fill="#ccc"><path d="M2 0L5 3L3.5 5Q5 8 7 8.5L9 7L12 10L10 12Q3 11 0 2Z"/></svg>+1 240 555 0147</div>
      <div class="row"><svg width="12" height="10" viewBox="0 0 12 10" fill="#ccc"><path d="M0 0H12V10H0ZM1 1L6 5L11 1Z"/></svg>info@brelvostudio.com</div>
      <div class="row"><svg width="10" height="13" viewBox="0 0 10 13" fill="#ccc"><path d="M5 0A5 5 0 0 1 10 5C10 8 5 13 5 13S0 8 0 5A5 5 0 0 1 5 0Z"/></svg>Map Direction</div>
    </div>
    <div class="map" role="img" aria-label="Street map showing the studio location"></div>
    <div class="footer-col newsletter">
      <h4>Newsletter</h4>
      <div class="field">Enter email address</div>
      <div class="send">Sign Up</div>
    </div>
  </div>
  <div class="footer-base">
    <span class="copy">Copyright © 2017. Company Name. All Right Reserved</span>
    <div class="social" aria-label="Social links"><span></span><span></span><span></span><span></span><span></span><span></span><span></span></div>
  </div>
</footer>

</body>
</html>
```